New Business card design to reflect rebrand

I would like a business card design with a good base colour for our new logo and also a placeholder for a profile pic of the card holder. the design needs to be editable to the point that we can easily change the picture of the person and use that design for printlarkly etc. we are looking at a metalic finish business card so will need a good base colour to bring out the finish.

Target Market(s)

prospective customers

Industry/Entity Type

Business

Contact Information for Business Card

I would like one editable design that we can change the name of the card holder and profile picture. The design need to be in a format that be send to printlarkly etc.

Our address is Fenwick Lodge, Mill Lane, Hartley Wintney, KT14 3WB Tel no. 01632 960418

Requirements
Must have
• place holder for a profile pic for the card holder. in AI or preferably PSD format

```html
<!DOCTYPE html>
<html lang="en">
<head>
<meta charset="utf-8">
<title>Quillorne Workplace Services – Business Card</title>
<link href="https://fonts.googleapis.com/css2?family=Lato:wght@400;700&display=swap" rel="stylesheet">
<style>
  :root {
    --brand-orange: #eb5e0b;
    --brand-slate: #425a79;
    --card-white: #ffffff;
    --stage: #eeeeee;
    --photo-light: #e9e9ea;
    --photo-mid: #cfc6c0;
    --photo-dark: #2a2b30;
  }
  html, body {
    margin: 0;
    padding: 0;
    width: 1200px;
    height: 1200px;
    overflow: hidden;
    background: var(--stage);
    font-family: "Lato", Arial, sans-serif;
  }
  .canvas {
    position: relative;
    width: 1200px;
    height: 1200px;
  }
  .card {
    position: absolute;
    left: 160px;
    width: 880px;
    height: 504px;
    box-shadow: 0 10px 30px rgba(0,0,0,0.18);
  }
  .card--front { top: 64px; }
  .card--back { top: 632px; }
  .card svg { display: block; width: 100%; height: 100%; }

  .fill-orange { fill: var(--brand-orange); }
  .fill-slate { fill: var(--brand-slate); }
  .fill-white { fill: var(--card-white); }

  .brand-name {
    font-family: "Lato", Arial, sans-serif;
    font-weight: 700;
    fill: var(--brand-slate);
  }
  .web-line {
    font-family: "Lato", Arial, sans-serif;
    font-size: 15px;
    letter-spacing: 3px;
    fill: var(--card-white);
  }
  .contact-text {
    font-family: "Lato", Arial, sans-serif;
    font-size: 12.5px;
    fill: var(--card-white);
  }
  .holder-name {
    font-family: "Lato", Arial, sans-serif;
    font-weight: 700;
    font-size: 16px;
    fill: var(--card-white);
  }
  .holder-title {
    font-family: "Lato", Arial, sans-serif;
    font-size: 12px;
    fill: var(--card-white);
  }
  .icon-box { fill: var(--brand-slate); }
  .icon-line { fill: none; stroke: var(--card-white); stroke-width: 1.2; stroke-linecap: round; stroke-linejoin: round; }
  .icon-solid { fill: var(--card-white); }
  .photo-frame { fill: url(#photoTone); stroke: var(--brand-slate); stroke-width: 2; }
</style>
</head>
<body>
<main class="canvas">

  <!-- Card front: brand side -->
  <section class="card card--front" aria-label="Business card front">
    <svg viewBox="0 0 561 321" xmlns="http://www.w3.org/2000/svg">
      <rect class="fill-orange" x="0" y="0" width="561" height="321"/>
      <path class="fill-white" d="M148 47 L472 47 Q487 47 482 61 L433 221 Q428 235 413 235 L90 235 Q75 235 80 221 L130 61 Q135 47 148 47 Z"/>
      <text class="brand-name" x="281" y="146" font-size="40" text-anchor="middle">QUILLORNE</text>
      <text class="brand-name" x="281" y="180" font-size="16" letter-spacing="3" text-anchor="middle">WORKPLACE SERVICES</text>
      <rect class="fill-slate" x="0" y="265" width="561" height="36"/>
      <text class="web-line" x="281" y="288" text-anchor="middle">www.website.com</text>
    </svg>
  </section>

  <!-- Card back: holder details -->
  <section class="card card--back" aria-label="Business card back">
    <svg viewBox="0 0 561 321" xmlns="http://www.w3.org/2000/svg">
      <defs>
        <linearGradient id="photoTone" x1="0" y1="0" x2="0" y2="1">
          <stop offset="0" stop-color="var(--photo-light)"/>
          <stop offset="0.55" stop-color="var(--photo-mid)"/>
          <stop offset="1" stop-color="var(--photo-dark)"/>
        </linearGradient>
      </defs>
      <rect class="fill-slate" x="0" y="0" width="561" height="321"/>
      <path class="fill-orange" d="M0 0 H561 V58 L537 262 Q533 285 510 285 H0 Z"/>
      <path class="fill-white" d="M0 0 H332 L302 176 Q296 205 266 205 H0 Z"/>

      <text class="brand-name" x="148" y="98" font-size="31" text-anchor="middle">QUILLORNE</text>
      <text class="brand-name" x="148" y="126" font-size="13" letter-spacing="2.6" text-anchor="middle">WORKPLACE SERVICES</text>

      <rect class="photo-frame" x="88" y="160" width="135" height="140" rx="10" role="img" aria-label="Profile photo of the card holder"/>

      <!-- mobile -->
      <g transform="translate(343 38)">
        <rect class="icon-box" width="16" height="16" rx="3"/>
        <rect class="icon-line" x="5" y="3" width="6" height="10" rx="1"/>
      </g>
      <text class="contact-text" x="368" y="51">+ 000 - 000 - 000</text>

      <!-- phone -->
      <g transform="translate(337 68)">
        <rect class="icon-box" width="16" height="16" rx="3"/>
        <path class="icon-solid" d="M5 3.5 L7 5.5 L6 7 Q7 9.5 9 10 L10.5 9 L12.5 11 L11 12.8 Q6.5 12.5 3.3 5 Z"/>
      </g>
      <text class="contact-text" x="362" y="81">+ 000 - 000 - 000</text>

      <!-- mail -->
      <g transform="translate(331 98)">
        <rect class="icon-box" width="16" height="16" rx="3"/>
        <rect class="icon-line" x="3.5" y="5" width="9" height="6.5" rx="0.8"/>
        <path class="icon-line" d="M3.8 5.4 L8 8.6 L12.2 5.4"/>
      </g>
      <text class="contact-text" x="356" y="111">mail@website.com</text>

      <!-- web -->
      <g transform="translate(325 129)">
        <rect class="icon-box" width="16" height="16" rx="3"/>
        <circle class="icon-line" cx="8" cy="8" r="4.8"/>
        <ellipse class="icon-line" cx="8" cy="8" rx="2" ry="4.8"/>
        <path class="icon-line" d="M3.2 8 H12.8"/>
      </g>
      <text class="contact-text" x="350" y="142">www.website.com</text>

      <!-- address -->
      <g transform="translate(319 164)">
        <rect class="icon-box" width="16" height="16" rx="3"/>
        <path class="icon-solid" d="M8 13 Q4.5 8.5 4.5 6.5 A3.5 3.5 0 0 1 11.5 6.5 Q11.5 8.5 8 13 Z"/>
        <circle class="fill-slate" cx="8" cy="6.5" r="1.3"/>
      </g>
      <text class="contact-text" x="345" y="176">Address: Street No, Nord</text>
      <text class="contact-text" x="345" y="192">Co,City/State Zipcode</text>

      <text class="holder-name" x="262" y="244">CARD HOLDER NAME</text>
      <text class="holder-title" x="262" y="268">JOB TITLE</text>
    </svg>
  </section>

</main>
</body>
</html>
```